Website refresh

We are a leading provide of JTAG hardware and software tools. We provide affordable USB and Ethernet solutions that are easily integrated into applications via a common API for Windows and Linux platforms. Our product simplicity, integration with third party applications, and free utilities have made us the provider of choice for Paragon100 companies, small businesses as well as academic and research institutions.

JTAG is an industry standard interface by which hardware and software engineers can debug, test and program their hardware or software.

Target Market(s)

We are in the technology industry, and our target audience includes hardware engineers, low level embedded software engineers, and ASIC designers.

Industry/Entity Type

Software

Requirements
Must have
• The artwork for the slider must incorporate the product photos provided.

Our new website will be a facelift for our current website (www.quillmarsh-kits.net), and must allow all the content on the current website to be incorporate into the new website (the new website may have a new CMS).
Nice to have
• Please use the screen sketches as guidance. It does not have to follow this exactly, but should allow for the various elements to be incorporated.

The design I liked is by Tomas Berenholt - his Harbor template.
http://tomasberenholt.net/templates/harbor/

here is the live demo:
http://tomasberenholt.net/files/demo/harbor/

What do you think about this? Would welcome your opinion. My product is in black plastic:
http://www.quillmarsh-kits.net/index.php?main_page=corvane

so I hope that some picture of this (to replace the photos in the templates) will work well. (I will need to include landing
pages like the one above into the new site, and there will be a few like this for other potential customers)

I would be also nice to exchange some ideas on the scrolling/rolling logos for customers (company logos) an partners (company logos)

Please let me know your thoughts.

If you are also able to do web programming, or work with someone who might be able to assist with web programming and migrating the website (while incorporating the new template), then please let me know separately.

```html
<!DOCTYPE html>
<html lang="en">
<head>
<meta charset="utf-8">
<title>Quillmarsh – JTAG cables and tools</title>
<link rel="stylesheet" href="https://fonts.googleapis.com/css2?family=Cabin:wght@400;600;700&family=Montserrat:wght@400;600;700&display=swap">
<style>
  :root {
    --ink: #222;
    --text: #444;
    --muted: #666;
    --purple: #7a3f95;
    --purple-deep: #5e0f6e;
    --banner-dark: #1c0614;
    --rule: #d6d6d6;
    --nav-top: #ffffff;
    --nav-bottom: #eeeeee;
    --box-bottom: #e3e3e8;
    --white: #fff;
  }
  * { box-sizing: border-box; margin: 0; padding: 0; }
  html, body { width: 1200px; height: 697px; overflow: hidden; background: var(--white); }
  body { position: relative; font-family: "Cabin", sans-serif; color: var(--text); border-top: 3px solid #000; }

  .brand { position: absolute; left: 180px; top: 10px; }
  .brand-name { font: 700 30px/1 "Cabin", sans-serif; color: var(--ink); letter-spacing: -0.3px; }
  .brand-tagline { margin-top: 8px; font-size: 12.5px; color: var(--ink); }

  .cart { position: absolute; left: 956px; top: -3px; width: 65px; height: 38px; background: #000; border-radius: 0 0 5px 5px;
          color: var(--white); display: flex; align-items: center; justify-content: center; gap: 5px; font: 400 15px "Montserrat", sans-serif; }

  .main-nav { position: absolute; left: 0; top: 73px; width: 1200px; height: 37px; border-top: 1px solid var(--rule); border-bottom: 1px solid var(--rule);
              background: linear-gradient(var(--nav-top), var(--nav-bottom)); }
  .main-nav ul { list-style: none; display: flex; margin-left: 180px; height: 100%; }
  .main-nav li { height: 100%; border-right: 1px solid var(--rule); display: flex; align-items: center; justify-content: center;
                 font: 400 14px "Montserrat", sans-serif; color: var(--ink); }
  .main-nav .is-active { background: var(--purple); color: var(--white); }

  .slider { position: absolute; left: 180px; top: 125px; width: 841px; height: 321px; border: 1px solid #ccc; border-radius: 3px; background: var(--white); }
  .slide { position: absolute; left: 9px; top: 8px; width: 822px; height: 305px; overflow: hidden;
           background: linear-gradient(90deg, var(--purple-deep) 0%, #6a1479 40%, var(--banner-dark) 62%, #2e0a22 100%); }
  .slide-curve { position: absolute; left: 0; top: 0; }
  .slide-product { position: absolute; left: 470px; top: 40px; width: 300px; height: 230px; border-radius: 20px;
                   background: radial-gradient(ellipse at 50% 60%, #8a8a90 0%, #4b3a44 45%, rgba(40,8,30,0) 75%); }
  .slide-title { position: absolute; left: 20px; top: 50px; font: 700 21px/1.1 "Montserrat", sans-serif; color: var(--white); text-transform: uppercase; }
  .slide-text { position: absolute; left: 20px; top: 112px; width: 250px; font: 400 14px/1.5 "Cabin", sans-serif; color: var(--white); }
  .slide-dots { position: absolute; left: 20px; top: 255px; display: flex; gap: 5px; }
  .slide-dots span { width: 14px; height: 14px; border-radius: 50%; background: var(--white); }
  .slide-dots .is-current { background: #000; }

  .panel { position: absolute; top: 528px; width: 258px; height: 98px; border: 1px solid #e8e8ec; border-top: none;
           background: linear-gradient(var(--white), var(--box-bottom)); }
  .panel-title { position: absolute; top: -63px; font: 400 21px "Cabin", sans-serif; color: var(--ink); }
  .news { left: 180px; }
  .news .panel-title { left: 25px; }
  .partners { left: 472px; }
  .partners .panel-title { left: 27px; }
  .customers { left: 764px; }
  .customers .panel-title { left: 27px; }

  .news-list { position: absolute; left: 26px; top: -17px; list-style: none; }
  .news-list li { margin-bottom: 12px; font-size: 12px; line-height: 1.35; color: var(--text); }
  .news-date { display: block; color: var(--purple); font-size: 11px; }

  .logo-frame { position: absolute; left: 29px; top: -18px; width: 200px; height: 102px; border: 1px solid #bdbdc2; border-radius: 5px;
                background: #e2e2e6; display: flex; align-items: center; justify-content: center; }
  .logo-card { width: 164px; height: 67px; background: var(--white); border: 1px solid #ccc; border-radius: 4px;
               display: flex; align-items: center; justify-content: center; text-align: center; }
  .partner-name { font: 700 22px "Cabin", sans-serif; color: #1b4f8c; }
  .client-placeholder { font: 400 15px/1.35 "Montserrat", sans-serif; color: var(--muted); }

  .site-footer { position: absolute; left: 0; top: 662px; width: 1200px; border-top: 1px solid var(--rule); height: 35px; }
  .copyright { position: absolute; left: 198px; top: 8px; font-size: 12px; color: var(--ink); }
  .footer-links { position: absolute; right: 195px; top: 10px; font-size: 12px; color: var(--ink); }
  .footer-links span { margin: 0 2px; }
</style>
</head>
<body>
  <header>
    <div class="brand">
      <div class="brand-name">Quillmarsh</div>
      <div class="brand-tagline">JTAG cables and tools for developers and engineers</div>
    </div>
    <div class="cart">
      <svg width="20" height="16" viewBox="0 0 20 16" aria-hidden="true"><path d="M1 1h3l2.5 9h10l2-7H5" fill="none" stroke="#fff" stroke-width="1.6"/><circle cx="8" cy="13.5" r="1.5" fill="#fff"/><circle cx="15" cy="13.5" r="1.5" fill="#fff"/></svg>
      <span>(0)</span>
    </div>
  </header>

  <nav class="main-nav">
    <ul>
      <li class="is-active" style="width:104px">PRODUCTS</li>
      <li style="width:119px">DOWNLOAD</li>
      <li style="width:94px">SUPPORT</li>
      <li style="width:72px">LOGIN</li>
    </ul>
  </nav>

  <section class="slider">
    <div class="slide">
      <svg class="slide-curve" width="822" height="305" viewBox="0 0 822 305" aria-hidden="true">
        <path d="M450 0 C330 40 270 140 260 305 L0 305 L0 0 Z" fill="#6a1479"/>
        <path d="M450 0 C330 40 270 140 260 305" fill="none" stroke="#9b4bb0" stroke-width="6" opacity="0.7"/>
      </svg>
      <div class="slide-product" role="img" aria-label="Photo of two JTAG interface units, one white and one black, standing upright"></div>
      <h1 class="slide-title">JTAG cables &amp; tools for<br>developers &amp; engineers</h1>
      <p class="slide-text">Lorem Ipsum is simply dummy text of the printing and typesetting industry. Lorem Ipsum has been the industry's standard dummy text ever since the 1500s.</p>
      <div class="slide-dots"><span class="is-current"></span><span></span><span></span><span></span><span></span></div>
    </div>
  </section>

  <section class="panel news">
    <h2 class="panel-title">News</h2>
    <ul class="news-list">
      <li><span class="news-date">28 March 2012</span>Lorem ipsum dolor sit amet contuer<br>adipiscing elit...</li>
      <li><span class="news-date">28 March 2012</span>Lorem ipsum dolor sit amet contuer<br>adipiscing elit...</li>
    </ul>
  </section>

  <section class="panel partners">
    <h2 class="panel-title">Partners</h2>
    <div class="logo-frame"><div class="logo-card"><span class="partner-name">Veltrica</span></div></div>
  </section>

  <section class="panel customers">
    <h2 class="panel-title">Customers</h2>
    <div class="logo-frame"><div class="logo-card"><span class="client-placeholder">Client’s Logo goes<br>here...</span></div></div>
  </section>

  <footer class="site-footer">
    <p class="copyright">© 2012Quillmarsh. All Rights Reserved.</p>
    <p class="footer-links">Terms &amp; conditions <span>|</span> Policy <span>|</span> Developers <span>|</span> About Us <span>|</span> Contact Us</p>
  </footer>
</body>
</html>
```